Marisol transparent business card

I would like to have a transparent business card created.
A simple yet classy card with
Website www.MarisolPennywhite.com
Phone # 555-417-2936
I would like my full photo on the card as well as my logo.

Target Market(s)

The business card will be printed on transparent card stock.
Www.MarisolPennywhite.com
Phone 555-417-2936
I would like my pic on the card and my logo
Author, Speaker, & Wealth architect

Industry/Entity Type

Business

Contact Information for Business Card

Www.MarisolPennywhite.com
Phone 555-417-2936

Font styles to use
Serif
Decorative
Script

Requirements
Must have
• The business card will be printed on transparent card stock.
• Www.MarisolPennywhite.com
• Phone 555-417-2936
• I would like my pic on the card and my logo
• Author, Speaker, & Wealth architect
Nice to have
• If I could have the tattoo on my pic blurred out or airbrushed over

```html
<!DOCTYPE html>
<html lang="en">
<head>
<meta charset="utf-8">
<title>Marisol Pennywhite – Business Card</title>
<link rel="stylesheet" href="https://fonts.googleapis.com/css2?family=Kalam:wght@400;700&family=Tinos:ital,wght@0,400;1,700&display=swap">
<style>
  :root {
    --canvas: #ffffff;
    --photo-light: #f5eeea;
    --photo-mid: #e6dcd6;
    --photo-dark: #2a2224;
    --sky-light: #cfe4f6;
    --sky-mid: #1a84da;
    --sky-deep: #1670c4;
    --navy: #20457f;
    --slate: #4a6fa6;
    --ink: #0d0d0d;
    --white: #ffffff;
  }
  * { margin: 0; padding: 0; box-sizing: border-box; }
  html, body {
    width: 1200px;
    height: 1000px;
    overflow: hidden;
    background: var(--canvas);
  }
  .canvas {
    position: relative;
    width: 1200px;
    height: 1000px;
  }
  .business-card {
    position: absolute;
    left: 168px;
    top: 308px;
    width: 704px;
    height: 364px;
    display: flex;
  }
  .portrait {
    width: 257px;
    height: 100%;
    background:
      radial-gradient(ellipse 38% 70% at 52% 72%, var(--photo-dark) 0%, var(--photo-dark) 55%, rgba(42,34,36,0) 75%),
      linear-gradient(180deg, var(--photo-light), var(--photo-mid));
  }
  .info-panel {
    position: relative;
    flex: 1;
    height: 100%;
    overflow: hidden;
    background:
      radial-gradient(ellipse 30% 40% at 100% 0%, var(--navy) 0%, rgba(32,69,127,0.6) 45%, rgba(32,69,127,0) 100%),
      radial-gradient(ellipse 70% 45% at 20% 18%, var(--sky-light) 0%, rgba(207,228,246,0.85) 45%, rgba(207,228,246,0) 100%),
      linear-gradient(90deg, rgba(0,0,0,0) 70%, rgba(74,111,166,0.9) 100%),
      linear-gradient(180deg, rgba(0,0,0,0) 75%, rgba(74,111,166,0.75) 100%),
      linear-gradient(160deg, var(--sky-mid) 0%, var(--sky-deep) 60%, var(--slate) 100%);
  }
  .name {
    position: absolute;
    left: 46px;
    top: 4px;
    font-family: "Kalam", cursive;
    font-weight: 400;
    font-size: 42px;
    color: var(--ink);
    white-space: nowrap;
  }
  .tagline {
    position: absolute;
    left: 35px;
    top: 64px;
    font-family: "Tinos", serif;
    font-style: italic;
    font-weight: 700;
    font-size: 25.5px;
    color: var(--ink);
    white-space: nowrap;
  }
  .phone {
    position: absolute;
    left: 8px;
    top: 246px;
    font-family: "Tinos", serif;
    font-size: 36px;
    letter-spacing: 0.6px;
    color: var(--white);
    white-space: nowrap;
  }
  .website {
    position: absolute;
    left: 6px;
    top: 302px;
    font-family: "Kalam", cursive;
    font-size: 25px;
    letter-spacing: -0.2px;
    color: var(--white);
    white-space: nowrap;
  }
  .website-label { margin-right: 10px; }
</style>
</head>
<body>
  <main class="canvas">
    <section class="business-card">
      <div class="portrait" role="img" aria-label="Full-length portrait of Marisol Pennywhite in a black dress, arms crossed, against a light wall"></div>
      <div class="info-panel">
        <h1 class="name">Marisol Pennywhite</h1>
        <p class="tagline">Author, Speaker, &amp; Wealth architect</p>
        <p class="phone">Phone # 555-417-2936</p>
        <p class="website"><span class="website-label">Website:</span>www.MarisolPennywhite.com</p>
      </div>
    </section>
  </main>
</body>
</html>
```